This book will apply the 12 Steps to gaming addiction, also known as video game addiction. The primary purpose of the book is to provide an effective solution for this new type of addiction. The solution is based on the rich and successful concepts of traditional twelve-step programs like RL.

The title on the cover will be "Nine Doors Past the Glowing Screen" and "by Martin Quorby". A subtitle can be used if it works in your design of "A Practical Path Beyond Compulsive Console Play". Cover will be for a 6" x 9" book approximately 110 pages in length.

Some back cover text including some review quotes and an author bio are in the attached Word doc. There is also an author photo attached for for the back cover.

Requirements
Must have
• For the cover design it could be stylized, or an image, a partial image, or whatever. I am open to suggestions. Think about what would be noticed by a person searching for help with moderating their video game use, or by the parents or loved ones of problem gamers. Something contemporary and eye catching.

```html
<!DOCTYPE html>
<html lang="en">
<head>
<meta charset="utf-8">
<title>Nine Doors Past the Glowing Screen – Back Cover</title>
<link rel="stylesheet" href="https://fonts.googleapis.com/css2?family=Bodoni+Moda:opsz,wght@6..96,700&display=swap">
<style>
  :root {
    --ink: #000000;
    --paper: #ffffff;
    --photo-leaf: #6f8a4a;
    --photo-brick: #7a4a36;
    --photo-light: #c9d6b0;
  }
  html, body {
    margin: 0;
    padding: 0;
    width: 800px;
    height: 1200px;
    overflow: hidden;
    background: var(--ink);
  }
  .back-cover {
    position: relative;
    width: 800px;
    height: 1200px;
    background: var(--ink);
    color: var(--paper);
    font-family: "Bodoni Moda", "Bodoni 72", Didot, serif;
    font-weight: 700;
    font-size: 13.6px;
    line-height: 17.9px;
    letter-spacing: -0.15px;
  }
  .text-panel {
    position: absolute;
    left: 128px;
    top: 61px;
    width: 529px;
    height: 919px;
    box-sizing: border-box;
    border: 8px solid var(--paper);
    background: var(--ink);
  }
  .block {
    position: absolute;
    left: 48px;
    width: 460px;
    margin: 0;
  }
  .praise-heading {
    left: 86px;
    top: 22px;
    font-size: 14.5px;
  }
  .quote { margin: 0; }
  .quote-source { display: block; }
  .divider {
    position: absolute;
    left: 13px;
    top: 464px;
    width: 487px;
    height: 3px;
    background: var(--paper);
  }
  .body-copy { line-height: 18.6px; }
  .section-heading {
    font-size: 14.5px;
    font-weight: 700;
  }
  .author-photo-frame {
    position: absolute;
    left: 330px;
    top: 1008px;
    width: 139px;
    height: 126px;
    box-sizing: border-box;
    border: 5px solid var(--paper);
    background: var(--ink);
    padding: 4px;
  }
  .author-photo {
    width: 100%;
    height: 100%;
    background: radial-gradient(ellipse at 50% 80%, #2a2c3a 0 35%, transparent 36%),
                linear-gradient(135deg, var(--photo-brick) 0%, var(--photo-leaf) 55%, var(--photo-light) 100%);
  }
</style>
</head>
<body>
<main class="back-cover">
  <section class="text-panel">
    <h2 class="block praise-heading" style="margin:0;">Praise for Nine Doors Past the Glowing Screen</h2>

    <blockquote class="block quote" style="top:44px;">
      “A must-read for anyone who is addicted to or thinks they may have a problem with digital gaming. This eloquent work will also be useful to academics and clinicians exploring potential solutions. The author recognizes the similarities between gaming addiction and other addictions, and logically applies one of the most effective known solutions for addiction - The Twelve Steps.”
      <cite class="quote-source" style="font-style:normal;">-- Dale Whitcombe, Noted Interventionist and Keynote Speaker</cite>
    </blockquote>

    <blockquote class="block quote" style="top:179px;">
      “If you suffer from digital gaming addiction, I strongly encourage you to use this book as your road map to get you back to the real world.”
      <cite class="quote-source" style="font-style:normal;">- Owen Lattimer, Founder of Signal Feed Review.</cite>
    </blockquote>

    <blockquote class="block quote" style="top:259px;">
      “As a high school teacher for 24 years, husband, father, coach, and 12-Step member, I can assure you that this book will transform the life of anyone who is addicted to video games. Well written, easy to understand, and a wonderful book that will provide you with a clear road map to recovery, and this includes teenagers, a group I have been working with in the classroom for decades.”
      <cite class="quote-source" style="font-style:normal;">-- Rafael Dorsey, Harbor Ridge, OR High School Teacher.</cite>
    </blockquote>

    <p class="block" style="top:410px;">An effective solution to the challenge of Digital Gaming Addiction (aka Video Game Addiction) based on the rich and successful tradition of the Twelve Steps.</p>

    <div class="divider" role="presentation"></div>

    <p class="block body-copy" style="top:490px;">Addiction to Digital Gaming is a new and troubling phenomenon that has burst upon an unprepared society with alarming speed. Many people crave the use of Digital Games in a strikingly similar way to any other addict. Digital Games are a complex software and hardware system that have been designed to promote continued and progressive usage. This sophisticated technology clearly feeds on natural addictive tendencies.</p>

    <p class="block body-copy" style="top:623px;">The 12 Steps are one of the most effective methods for treating addiction in human history. Originating with the Recovery League in 1939, the 12 Steps have since been used to treat a variety of other addictions, including drugs, sex, gambling, eating disorders, and many others. Now in this groundbreaking work the 12 Steps are applied to the complex and evolving contemporary phenomenon of Digital Gaming Addiction.</p>

    <h3 class="block section-heading" style="top:765px; margin:0;">About the Author</h3>

    <p class="block body-copy" style="top:791px;">Martin Quorby is a Technology Consultant and Writer with many years of professional coding and consulting experience. He also struggled with addiction to drugs and alcohol and is now clean and sober in a Twelve-Step program for over 17 years. This unique combination of 12-Step experience and technology expertise led him to create Nine Doors Past the Glowing Screen.</p>
  </section>

  <figure class="author-photo-frame" style="margin:0;">
    <div class="author-photo" role="img" aria-label="Portrait photo of the author, Martin Quorby, outdoors against greenery"></div>
  </figure>
</main>
</body>
</html>
```